Business Card for Bright Meadow Lawn & Landscape

Double Sided Card Design - I think one side of the card should be cleaner, with logo, contact info, and "Complete Residential & Commercial Landscape Services", and on the other side it should list the services we offer:

- Lawn Care & Mowing
- Hedge & Shrub Trimming
- Leaf Removal & Clean Up
- Aeration & Sod
- Mulch & Rock Installations
- Landscape Installations & Renovations
- Commercial Snow Removal

Please make it clean and very professional... don't want it too be too busy, but want to tell them what we do.

Target Market(s)

Residential and Commercial

Industry/Entity Type

Landscape

Contact Information for Business Card

Fully Insured
Tom Berrigan
410-555-0198
Tberrigan07@mailbox-example.com

Requirements
Must have
• Double Sided, Cleaner on one side, more information and text on the other side.

```html
<!DOCTYPE html>
<html lang="en">
<head>
<meta charset="utf-8">
<title>Bright Meadow Lawn &amp; Landscape – Business Card</title>
<link href="https://fonts.googleapis.com/css2?family=Arvo:wght@400;700&display=swap" rel="stylesheet">
<style>
  :root {
    --backdrop: #a4a4a4;
    --card-center: #1c1c1c;
    --card-edge: #050505;
    --green: #7cc242;
    --white: #f4f4f4;
    --divider: #3a3a3a;
  }
  * { box-sizing: border-box; margin: 0; padding: 0; }
  html, body { width: 1200px; height: 1200px; overflow: hidden; }
  body {
    background: var(--backdrop);
    font-family: "Arvo", Georgia, serif;
    display: flex;
    flex-direction: column;
    align-items: center;
    justify-content: center;
    gap: 90px;
  }
  .card {
    width: 700px;
    height: 400px;
    border-radius: 38px;
    background: radial-gradient(ellipse at 45% 40%, var(--card-center) 0%, var(--card-edge) 75%);
    box-shadow: 0 18px 40px rgba(0,0,0,0.35);
    display: flex;
    align-items: center;
    justify-content: center;
  }
  .divider {
    width: 1px;
    align-self: center;
    background: var(--divider);
    margin: 0 22px;
  }

  /* Services side */
  .brand {
    display: flex;
    flex-direction: column;
    align-items: center;
    gap: 14px;
    width: 200px;
  }
  .brand-mark {
    width: 64px; height: 64px;
  }
  .brand-name {
    color: var(--green);
    font-weight: 400;
    font-size: 19px;
    line-height: 1.3;
    text-align: center;
  }
  .services .divider { height: 150px; }
  .service-list {
    list-style: none;
    font-weight: 700;
    font-size: 16px;
    line-height: 1.45;
  }
  .service-list li:nth-child(odd) { color: var(--green); }
  .service-list li:nth-child(even) { color: var(--white); }

  /* Contact side */
  .identity {
    display: flex;
    flex-direction: column;
    align-items: flex-end;
  }
  .person-name {
    color: var(--white);
    font-weight: 700;
    font-size: 30px;
    letter-spacing: -0.5px;
    text-transform: uppercase;
  }
  .insured {
    color: var(--white);
    font-size: 17px;
  }
  .contact .divider { height: 110px; }
  .contact-details {
    font-size: 15px;
    line-height: 1.5;
    color: var(--white);
  }
  .contact-row .label {
    color: var(--green);
    display: inline-block;
    width: 52px;
  }
  .tagline {
    margin-top: 6px;
    font-weight: 700;
    font-size: 15px;
    line-height: 1.35;
  }
</style>
</head>
<body>

  <section class="card services" aria-label="Services side">
    <div class="brand">
      <svg class="brand-mark" viewBox="0 0 64 64" aria-hidden="true">
        <circle cx="32" cy="32" r="28" fill="none" stroke="var(--green)" stroke-width="5"/>
      </svg>
      <p class="brand-name">Bright Meadow<br>Lawn &amp; Landscape</p>
    </div>
    <div class="divider"></div>
    <ul class="service-list">
      <li>Lawn Care &amp; Mowing</li>
      <li>Hedge &amp; Shrub Trimming</li>
      <li>Leaf Removal &amp; Clean Up</li>
      <li>Aeration &amp; Sod</li>
      <li>Mulch &amp; Rock Installations</li>
      <li>Landscape Installations &amp; Renovations</li>
      <li>Commercial Snow Removal</li>
    </ul>
  </section>

  <section class="card contact" aria-label="Contact side">
    <div class="identity">
      <h1 class="person-name">Tom Berrigan</h1>
      <p class="insured">Fully Insured</p>
    </div>
    <div class="divider"></div>
    <div class="contact-details">
      <p class="contact-row"><span class="label">Tel</span>: 410-555-0198</p>
      <p class="contact-row"><span class="label">Email</span>: Tberrigan07@mailbox-example.com</p>
      <p class="tagline">Complete Residential &amp;<br>Commercial Landscape Services</p>
    </div>
  </section>

</body>
</html>
```